BRIARWOOD LOUNGE FRIDAY MAY 3

Flyer design for bar/nightclub event. Trying to keep a general theme with their flyers (see below) but would like to add some neon or some pop to it.

TEXT:

Briarwood Bar & Lounge Presents

LANTERN NIGHTS
GRAND OPENING EVENT

PURE HOUSE MUSIC W/

VORTEX
MARCO TELLEN
BRANDT & DJ WOBNIX

21+
9PM-130AM
712 K AVENUE DAVIS CA

Target Market(s)

House/dance music crowd.

Industry/Entity Type

Night Club

Font styles to use
Sans Serif

Colors
9bcb3c
fbee3d
ffffff

Requirements
Must have
• Large DJ names
Nice to have
• General theme of the attached flyers. Neon colors that stick with the theme. Anything else that looks cool will be considered

```html
<!DOCTYPE html>
<html lang="en">
<head>
<meta charset="utf-8">
<title>Briarwood Lounge – Lantern Nights Grand Opening</title>
<link href="https://fonts.googleapis.com/css2?family=Montserrat:wght@600;700;800&family=Oswald:wght@700&family=Alegreya+Sans+SC:wght@800&family=Bangers&display=swap" rel="stylesheet">
<style>
  :root {
    --night: #0b1430;
    --black: #050505;
    --neon-green: #9bcb3c;
    --neon-yellow: #fbee3d;
    --white: #ffffff;
    --orb: #0d1831;
    --glow: #7ff6ff;
  }
  html, body {
    margin: 0;
    padding: 0;
    overflow: hidden;
    background: var(--black);
  }
  .flyer {
    position: relative;
    width: 848px;
    height: 1200px;
    overflow: hidden;
    background: var(--black);
    font-family: "Montserrat", sans-serif;
    color: var(--white);
  }
  .campfire-scene {
    position: absolute;
    inset: 0;
    background:
      radial-gradient(ellipse 190px 330px at 330px 930px, rgba(255,225,140,.95), rgba(255,140,40,.7) 40%, rgba(200,60,10,.25) 75%, transparent 100%),
      radial-gradient(ellipse 420px 360px at 330px 1000px, rgba(255,110,20,.45), transparent 80%),
      radial-gradient(ellipse 300px 120px at 120px 960px, rgba(150,60,20,.45), transparent 80%),
      linear-gradient(180deg, var(--night) 0%, #0a1226 25%, #07080d 50%, var(--black) 100%);
  }
  .headline-top {
    position: absolute;
    top: 20px;
    left: 0;
    width: 848px;
    text-align: center;
    font-weight: 700;
    font-size: 30px;
    letter-spacing: 21px;
    padding-left: 21px;
    box-sizing: border-box;
    white-space: nowrap;
  }
  .brand-mark {
    position: absolute;
    top: 225px;
    left: 0;
    width: 848px;
    display: flex;
    justify-content: center;
    align-items: center;
    gap: 14px;
    font-family: "Alegreya Sans SC", sans-serif;
    font-weight: 800;
    font-size: 40px;
    letter-spacing: 4px;
    color: var(--neon-green);
  }
  .brand-mark .dot {
    width: 18px;
    height: 18px;
    border-radius: 50%;
    background: var(--neon-green);
  }
  .presenter {
    position: absolute;
    top: 336px;
    left: 0;
    width: 848px;
    text-align: center;
    font-family: "Alegreya Sans SC", sans-serif;
    font-weight: 800;
    font-size: 24px;
  }
  .event-name, .event-type, .happy-hour {
    position: absolute;
    left: 0;
    width: 848px;
    text-align: center;
    font-family: "Oswald", sans-serif;
    font-weight: 700;
    text-transform: uppercase;
    white-space: nowrap;
  }
  .event-name {
    top: 372px;
    font-size: 42px;
    letter-spacing: 2px;
    color: var(--neon-yellow);
  }
  .event-type {
    top: 420px;
    font-size: 60px;
    letter-spacing: 3px;
    color: var(--neon-yellow);
  }
  .lineup-orb {
    position: absolute;
    left: 490px;
    top: 544px;
    width: 384px;
    height: 384px;
    border-radius: 50%;
    background: radial-gradient(circle, #142246 0%, var(--orb) 70%, #0a1128 100%);
    box-shadow:
      0 0 0 4px rgba(255,255,255,.85),
      0 0 18px 8px var(--glow),
      0 0 60px 20px rgba(120,240,255,.45),
      inset 0 0 30px rgba(120,240,255,.35);
  }
  .lineup {
    position: absolute;
    top: 586px;
    left: 522px;
    width: 300px;
    margin: 0;
    padding: 0;
    list-style: none;
    text-align: center;
    font-family: "Bangers", sans-serif;
    font-size: 38px;
    line-height: 54px;
    letter-spacing: 1px;
    color: var(--neon-green);
    text-transform: uppercase;
    white-space: nowrap;
    transform: skewX(-6deg);
  }
  .happy-hour {
    top: 1072px;
    font-size: 48px;
    letter-spacing: 2px;
    color: var(--neon-green);
  }
  .address {
    position: absolute;
    top: 1140px;
    left: 0;
    width: 848px;
    text-align: center;
    font-weight: 800;
    font-size: 20px;
    white-space: nowrap;
  }
  .address .age {
    color: var(--neon-yellow);
    margin-right: 14px;
  }
</style>
</head>
<body>
  <div class="flyer">
    <div class="campfire-scene" role="img" aria-label="Campfire burning at night in a pine forest, sparks rising, people seated around the fire"></div>

    <div class="headline-top">PURE HOUSE MUSIC W/</div>

    <div class="brand-mark"><span class="dot"></span>BRIARWOOD</div>

    <div class="presenter">Briarwood Bar &amp; Lounge Presents</div>
    <div class="event-name">Lantern Nights</div>
    <div class="event-type">Grand Opening Event</div>

    <div class="lineup-orb"></div>
    <ul class="lineup">
      <li>DJ</li>
      <li>Vortex</li>
      <li>Marco Tellen</li>
      <li>Mr. Halvern</li>
      <li>Brandt &amp; DJ Wobnix</li>
    </ul>

    <div class="happy-hour">Happy Hour 9PM-130AM</div>
    <div class="address"><span class="age">21+</span>712 K AVENUE DAVIS CA</div>
  </div>
</body>
</html>
```